Quimby's Yard & Garden Center Business Card Update

I need an updated Business card design for my Lawn and Garden Center. We do Landscaping installs, Lawn Mowing, Snow Removal and also have a Garden Center Retail Division. I uploaded a few of our previous business cards to give an idea of what we are starting with. The main goal of this update is to simplify and modernize the business card, not all of the services that are on the previous cards has to be on the new one but I would still like to highlight our main services. There is also a sample of our logo that Can be used in the design.

Industry/Entity Type

Landscaping

Contact Information for Business Card

Morris Quimby
Morris@Quimbysyardandgarden.example
Business (555) 201-7784
Cell (555) 318-6092

Colors

Designer to choose colors to be used in the design.

Requirements
Must have
• Services Provided :
• Landscaping
• Lawn Maintenance
• Snow Removal
• Garden Center

```html
<!DOCTYPE html>
<html lang="en">
<head>
<meta charset="utf-8">
<title>Quimby's Yard & Garden Center – Business Card</title>
<link href="https://fonts.googleapis.com/css2?family=Open+Sans:wght@400;600;700&display=swap" rel="stylesheet">
<style>
  :root {
    --stage: #2a2a2a;
    --card: #ffffff;
    --green: #2d5a27;
    --green-dark: #234a1f;
    --ink: #444444;
    --ink-soft: #555555;
    --snow-1: #eef1f5;
    --snow-2: #c9ced6;
    --house: #b8b0a2;
  }
  * { box-sizing: border-box; margin: 0; padding: 0; }
  html, body {
    width: 1200px; height: 900px; overflow: hidden;
    background: var(--stage);
    font-family: "Open Sans", Arial, sans-serif;
  }
  .stage {
    position: relative; width: 1200px; height: 900px;
    display: flex; flex-direction: column; align-items: center;
    justify-content: center; gap: 30px;
  }
  .card {
    position: relative; width: 700px; height: 400px;
    background: var(--card); overflow: hidden;
  }

  /* brand name */
  .brand {
    position: absolute; display: flex; align-items: center; gap: 14px;
  }
  .brand-mark {
    width: 34px; height: 34px; border-radius: 50%;
    background: var(--green);
  }
  .brand-name {
    font-weight: 700; font-size: 44px; color: var(--green);
    letter-spacing: 0.5px;
  }

  /* front */
  .card-front .brand { left: 70px; top: 90px; }
  .front-photo {
    position: absolute; right: 0; top: 0; width: 440px; height: 100%;
    background:
      linear-gradient(90deg, #ffffff 0%, rgba(255,255,255,0) 35%),
      linear-gradient(180deg, var(--house) 0%, #d8d4cc 40%, var(--snow-2) 62%, var(--snow-1) 100%);
  }
  .services { position: absolute; left: 60px; top: 270px; }
  .services-title {
    font-size: 17px; font-weight: 600; color: var(--green);
    padding-bottom: 4px; border-bottom: 1px solid var(--green);
    display: inline-block; margin-bottom: 8px;
  }
  .services-list {
    list-style: none; display: grid;
    grid-template-columns: auto auto; column-gap: 22px; row-gap: 6px;
    font-size: 17px; color: var(--ink-soft);
  }
  .services-list li::before {
    content: ""; display: inline-block; width: 8px; height: 8px;
    border: 1px solid var(--ink-soft); border-radius: 50%;
    margin-right: 6px; vertical-align: middle;
  }

  /* back */
  .card-back .brand { left: 60px; top: 50px; }
  .back-photo {
    position: absolute; right: 20px; top: 90px; width: 330px; height: 270px;
    background: radial-gradient(ellipse at 55% 55%, #e46a2a 0%, #5a5a5a 35%, #9a9a9a 55%, #ffffff 75%);
  }
  .contact { position: absolute; left: 0; top: 150px; }
  .name-block {
    border-left: 12px solid var(--green); padding-left: 40px;
  }
  .person-name { font-size: 26px; font-weight: 700; color: var(--green); line-height: 1.1; }
  .person-title { font-size: 14px; color: var(--ink); }
  .divider { width: 26px; height: 1px; background: var(--green); margin: 6px 0 8px 52px; }
  .details { padding-left: 52px; font-size: 17px; color: var(--ink-soft); line-height: 1.35; }
  .details .row { display: flex; align-items: center; gap: 10px; margin-left: -28px; }
  .details .row svg { width: 16px; height: 16px; flex: none; fill: var(--green); }
  .bottom-band {
    position: absolute; left: 0; bottom: 0; width: 100%; height: 10px;
    background: var(--green-dark);
  }
</style>
</head>
<body>
<main class="stage">

  <section class="card card-front">
    <div class="front-photo" role="img" aria-label="Company pickup truck plowing snow in front of houses"></div>
    <div class="brand">
      <span class="brand-mark"></span>
      <span class="brand-name">Quimby's</span>
    </div>
    <div class="services">
      <h2 class="services-title">Our Main Services</h2>
      <ul class="services-list">
        <li>Landscaping</li>
        <li>Snow Removal</li>
        <li>Lawn Maintenance</li>
        <li>Garden Center</li>
      </ul>
    </div>
  </section>

  <section class="card card-back">
    <div class="brand">
      <span class="brand-mark"></span>
      <span class="brand-name">Quimby's</span>
    </div>
    <div class="back-photo" role="img" aria-label="Orange and black commercial ride-on mower"></div>
    <div class="contact">
      <div class="name-block">
        <div class="person-name">Morris Quimby</div>
        <div class="person-title">Managing Director</div>
      </div>
      <div class="divider"></div>
      <div class="details">
        <div>48 Maple Row</div>
        <div>Fairhaven, OH 45599</div>
        <div class="row">
          <svg viewBox="0 0 24 24" aria-hidden="true"><path d="M3 9c0-2 4-4 9-4s9 2 9 4v2h-5V9H8v2H3zM6 12h12l2 8H4z"/></svg>
          <span>(555) 201-7784</span>
        </div>
        <div class="row">
          <svg viewBox="0 0 24 24" aria-hidden="true"><path d="M6 2l4 4-2 3c1 3 4 6 7 7l3-2 4 4-3 3C10 21 3 14 2 5z"/></svg>
          <span>(555) 318-6092</span>
        </div>
        <div class="row">
          <svg viewBox="0 0 24 24" aria-hidden="true"><path d="M2 5h20v14H2zm2 2v1l8 5 8-5V7l-8 5z"/></svg>
          <span>Morris@Quimbysyardandgarden.example</span>
        </div>
        <div class="row">
          <svg viewBox="0 0 24 24" aria-hidden="true"><circle cx="12" cy="12" r="10"/></svg>
          <span>www.quimbysyardandgarden.example</span>
        </div>
      </div>
    </div>
    <div class="bottom-band"></div>
  </section>

</main>
</body>
</html>
```